Games for Classrooms Website Redesign

The purpose of the website redesign is to freshen up the content and update it to give a more modern look and feel. It will show what we do concisely and satisfy all potential visitors. We work with primary schools and the brand is fun.About: Games for Classrooms is a scheme that brings top Olympic athletes into primary schools to inspire children to do more physical activity. We typically run a half day event at the school where the athlete does a fun fitness circuit with the children and then an inspirational assembly with a demonstration and Q&A. The children are asked to collect sponsorship money to take part in the event and a large proportion of the money raised goes back to the school in the form of a voucher for them to spend on new sports equipment. 1. To generate more leads from potential customers/schools2. To engage the children and parents more in the event and get them excited for their upcoming visit whilst setting up a fundraiser page.3. To simplify and modernise what is already there.

I have attached some ideas for each of the pages (uploaded in brief)

Here is a link to our current website: www.gamesforclassrooms.org

I have also attached a link to the sponsorship form which shows the kind of look and feel we're after.

Target Market(s)

Primary school teachers
Primary school parents

Number of Pages Required

5+ page

Requirements
Must have
• Fun, modern.
• Be built on twitter bootstrap

```html
<!DOCTYPE html>
<html lang="en">
<head>
<meta charset="utf-8">
<title>Games for Classrooms – Home</title>
<link href="https://fonts.googleapis.com/css2?family=Baloo+2:wght@500;600;700&family=Roboto+Slab:wght@300;400&family=Montserrat:wght@600&display=swap" rel="stylesheet">
<style>
  :root{
    --red:#f4351e;
    --red-deep:rgba(120,0,0,.30);
    --green:#6cbd45;
    --green-soft:#d9eecd;
    --blue:#2aa3e3;
    --cyan:#1fc8f0;
    --cyan-soft:#c8f1fb;
    --sky:#1aa3d9;
    --orange:#f07a1a;
    --ink:#1d1d1d;
    --white:#ffffff;
  }
  *{margin:0;padding:0;box-sizing:border-box}
  html,body{width:1200px;height:1200px;overflow:hidden;background:var(--white)}
  .page{position:absolute;left:204px;top:0;width:792px;height:1200px;background:var(--red);overflow:hidden;font-family:"Roboto Slab",Georgia,serif}
  .hero-art{position:absolute;left:0;top:0}

  .brand{position:absolute;left:98px;top:14px;display:flex;flex-direction:column}
  .brand .tagline{font-family:"Baloo 2",sans-serif;font-weight:500;font-size:12px;color:var(--red);margin-left:38px;line-height:1.1}
  .brand .name{display:flex;align-items:center;gap:6px;font-family:"Baloo 2",sans-serif;font-weight:600;font-size:14px;color:var(--ink);line-height:1.1;margin-top:2px}
  .brand .dot{width:26px;height:26px;border-radius:50%;background:var(--blue)}

  .nav{position:absolute;left:316px;top:29px;display:flex;align-items:center;gap:9px;font-family:"Baloo 2",sans-serif;font-weight:600;font-size:9.5px;list-style:none;white-space:nowrap}
  .nav li.sep{width:3px;height:3px;border-radius:50%;background:#8a8a8a}
  .nav .n1{color:var(--red)} .nav .n2{color:var(--green)} .nav .n3{color:var(--blue)} .nav .n4{color:var(--orange)} .nav .n5{color:var(--cyan)}
  .search{position:absolute;left:674px;top:27px;width:18px;height:18px;border-radius:50%;background:var(--green)}

  .intro{position:absolute;left:98px;top:76px;width:238px;height:226px;background:var(--blue);border-radius:18px;padding:16px 20px 0 24px;color:var(--white)}
  .intro h1{font-family:"Baloo 2",sans-serif;font-weight:600;font-size:16.5px;line-height:1.3;margin-bottom:8px;white-space:nowrap}
  .intro p{font-size:8.4px;font-weight:300;line-height:12.9px}

  .card{position:absolute;top:452px;height:240px;background:var(--white);text-align:center;z-index:1}
  .card.school{left:118px;width:256px;border:6px solid var(--green)}
  .card.parent{left:410px;width:256px;border:6px solid var(--cyan);border-radius:12px}
  .card .badge{position:relative;margin:20px auto 0;width:106px;height:106px;border-radius:50%}
  .card.school .badge{background:var(--green-soft)}
  .card.parent .badge{background:var(--cyan-soft)}
  .card .badge svg{position:absolute;left:7px;top:7px;width:92px;height:92px}
  .card h2{font-family:"Baloo 2",sans-serif;font-weight:600;font-size:31px;color:var(--ink);margin-top:6px;line-height:1.2;white-space:nowrap}
  .card .more{font-family:"Montserrat",sans-serif;font-weight:600;font-size:6px;letter-spacing:1.2px;color:#333;margin-top:6px}
  .card.school .more b{color:var(--green)}
  .card.parent .more b{color:var(--cyan)}

  .art{position:absolute;z-index:2}
  .art.supplies{left:168px;top:424px;width:84px;height:26px;border-radius:13px 13px 4px 4px;background:linear-gradient(90deg,#f7c948,#e8e2d6,#f2a23a)}
  .art.bulb{left:112px;top:440px;width:34px;height:40px;border-radius:17px 17px 10px 10px;background:#f7c948}
  .art.clock{left:110px;top:646px;width:44px;height:44px;border-radius:50%;background:#e13b2f;box-shadow:inset 0 0 0 6px #e13b2f,inset 0 0 0 20px #ffffff}
  .art.compass{left:356px;top:446px;width:10px;height:84px;border-radius:5px;background:#c9322a}
  .art.books{left:350px;top:598px;width:52px;height:96px;border-radius:26px 26px 4px 4px;background:linear-gradient(#2f7fb8 0,#2f7fb8 44%,#f3d7a0 44%,#f3d7a0 62%,#c23b2e 62%,#c23b2e 80%,#f3d7a0 80%)}
  .art.figures{left:626px;top:520px;width:80px;height:166px;border-radius:40px 40px 6px 6px;background:linear-gradient(#2d4a8a 0,#2d4a8a 55%,#3a3a4a 55%,#3a3a4a 100%)}

  .stats-title{position:absolute;left:0;width:792px;top:766px;font-family:"Baloo 2",sans-serif;font-weight:700;font-size:28px;color:var(--white);display:flex;justify-content:center;align-items:center;gap:10px}
  .stats-title i{width:32px;height:32px;border-radius:50%;background:var(--white)}
  .stat{position:absolute;top:830px;width:174px;height:117px;background:var(--red-deep);border-radius:6px;color:var(--white);text-align:center}
  .stat strong{display:block;font-family:"Baloo 2",sans-serif;font-weight:700;font-size:34px;line-height:1;margin-top:26px}
  .stat span{display:block;font-size:17px;font-weight:300;line-height:1.25;margin-top:8px}
  .stat.money strong{margin-top:18px}
  .stat.money span{margin-top:6px}

  .footer-shape{position:absolute;left:0;top:0}
  .signup{position:absolute;left:420px;top:1024px;width:266px;text-align:center;color:var(--white)}
  .signup h3{font-family:"Baloo 2",sans-serif;font-weight:600;font-size:18px;margin-bottom:10px}
  .signup form{display:flex;height:33px}
  .signup .field{flex:1;background:var(--white);font-size:10px;color:#555;text-align:left;padding:10px 18px}
  .signup .send{width:54px;background:var(--red);font-size:11px;padding-top:9px}
  .links{position:absolute;left:400px;width:310px;top:1117px;text-align:center;font-size:9.5px;color:var(--white);white-space:nowrap}
  .legal{position:absolute;left:390px;width:330px;top:1151px;text-align:center;font-size:7px;color:var(--white);line-height:9.6px}
  .legal p:first-child{margin-bottom:4px}
  .social{position:absolute;top:1166px;left:202px;display:flex;gap:13px}
  .social span{width:24px;height:24px;border-radius:50%;background:var(--white)}
</style>
</head>
<body>
<main class="page">
  <svg class="hero-art" width="792" height="420" viewBox="0 0 792 420">
    <defs>
      <linearGradient id="photoTone" x1="0" x2="1" y1="0" y2="0.35">
        <stop offset="0.3" stop-color="#ffffff"/>
        <stop offset="0.5" stop-color="#efe7dc"/>
        <stop offset="0.66" stop-color="#e2d2bd"/>
        <stop offset="0.8" stop-color="#9fc9a3"/>
        <stop offset="1" stop-color="#4c64a4"/>
      </linearGradient>
      <linearGradient id="topFade" x1="0" x2="0" y1="0" y2="1">
        <stop offset="0" stop-color="#ffffff" stop-opacity="0.95"/>
        <stop offset="0.18" stop-color="#ffffff" stop-opacity="0"/>
      </linearGradient>
      <clipPath id="heroClip">
        <path d="M0,256 C50,320 140,335 200,325 C240,318 260,350 300,370 C360,400 420,395 480,372 C560,340 620,300 680,280 C730,262 770,230 792,192 L792,0 L0,0 Z"/>
      </clipPath>
    </defs>
    <g clip-path="url(#heroClip)" role="img" aria-label="Photo of children doing a fitness circuit with an athlete in a school hall">
      <rect width="792" height="420" fill="url(#photoTone)"/>
      <rect width="792" height="420" fill="url(#topFade)"/>
    </g>
    <path d="M0,256 C50,320 140,335 200,325 C240,318 260,350 300,370 C360,400 420,395 480,372 C560,340 620,300 680,280 C730,262 770,230 792,192" fill="none" stroke="var(--green)" stroke-width="11"/>
  </svg>

  <header>
    <div class="brand">
      <span class="tagline">2 million kids inspired</span>
      <span class="name"><span class="dot"></span>Games for Classrooms</span>
    </div>
    <ul class="nav">
      <li class="n1">Athlete Visits</li><li class="sep"></li>
      <li class="n2">Get Active</li><li class="sep"></li>
      <li class="n3">Our Athletes</li><li class="sep"></li>
      <li class="n4">About Us</li><li class="sep"></li>
      <li class="n5">Clubs for Schools</li>
    </ul>
    <svg class="search" viewBox="0 0 18 18"><circle cx="9" cy="9" r="9" fill="#6cbd45"/><circle cx="8" cy="8" r="3.2" fill="none" stroke="#fff" stroke-width="1.4"/><line x1="10.4" y1="10.4" x2="12.6" y2="12.6" stroke="#fff" stroke-width="1.6" stroke-linecap="round"/></svg>
  </header>

  <section class="intro">
    <h1>Let’s inspire a Generation</h1>
    <p>1,300 Primary Schools nationwide receive a visit annually; that’s over 350,000 kids each year who will forever remember the day an International or Olympic athlete dropped into their school! Each of those 350,000 kids will have taken part in an exciting fitness circuit with an athlete and enjoyed an inspirational assembly. The outcome is a great sense of achievement, and being part of a scheme that has helped to raise over £2.6m for schools and sports equipment to date!</p>
  </section>

  <div class="art supplies" role="img" aria-label="Illustration of pencils, ruler and eraser"></div>
  <div class="art bulb" role="img" aria-label="Illustration of a light bulb"></div>
  <div class="art compass" role="img" aria-label="Illustration of a drawing compass"></div>
  <div class="art clock" role="img" aria-label="Illustration of an alarm clock"></div>
  <div class="art books" role="img" aria-label="Illustration of a globe on a stack of books"></div>

  <article class="card school">
    <div class="badge" role="img" aria-label="School building icon">
      <svg viewBox="0 0 92 92"><circle cx="46" cy="46" r="46" fill="#6cbd45"/><path d="M26 62 V42 H66 V62 M22 42 L46 28 L70 42 M40 62 V52 H52 V62 M46 28 V18 H54" fill="none" stroke="#fff" stroke-width="2" stroke-linejoin="round"/></svg>
    </div>
    <h2>I’m a School</h2>
    <p class="more">LEARN MORE <b>▸</b></p>
  </article>

  <article class="card parent">
    <div class="badge" role="img" aria-label="Family icon">
      <svg viewBox="0 0 92 92"><circle cx="46" cy="46" r="46" fill="#1fc8f0"/><g fill="none" stroke="#fff" stroke-width="2"><circle cx="36" cy="36" r="7"/><circle cx="56" cy="36" r="7"/><circle cx="46" cy="52" r="5"/><path d="M24 64 C24 52 48 50 48 50 M68 64 C68 52 44 50 44 50 M38 68 C38 60 54 60 54 68"/></g></svg>
    </div>
    <h2>I’m a Parent</h2>
    <p class="more">LEARN MORE <b>▸</b></p>
  </article>
  <div class="art figures" role="img" aria-label="Illustration of a teacher standing with a pupil"></div>

  <h2 class="stats-title"><i></i>Our Statistics</h2>
  <div class="stat" style="left:120px"><strong>1,300</strong><span>Primary Schools</span></div>
  <div class="stat" style="left:313px"><strong>350,000</strong><span>Kids each year</span></div>
  <div class="stat money" style="left:506px"><strong>£2.6m</strong><span>Schools &amp; Sports Equipment</span></div>

  <svg class="footer-shape" width="792" height="1200" viewBox="0 0 792 1200">
    <path d="M140,1200 C230,1070 400,990 565,1000 C680,1008 760,1060 792,1112 L792,1200 Z" fill="var(--sky)" stroke="#ffffff" stroke-width="2"/>
  </svg>

  <footer>
    <div class="signup">
      <h3>Sign up for latest news</h3>
      <form><span class="field">Enter your email id</span><span class="send">Send</span></form>
    </div>
    <p class="links">Sitemap &nbsp;|&nbsp; Cookies &nbsp;|&nbsp; Privacy Policy &nbsp;|&nbsp; Online Fundraising</p>
    <div class="legal">
      <p>© 2019 Games for Classrooms</p>
      <p>Games for Classrooms and GFC Coaching are trading names of the Social Enterprise called Playwell Ventures Limited, a company registered in England no. 00000000.</p>
    </div>
    <div class="social"><span></span><span></span><span></span></div>
  </footer>
</main>
</body>
</html>
```